Business Management Fortress

Assist with enhancing a powerpoint slide by providing a few design options for consideration. I have a template but open to any creative ideas.

Target Market(s)

Internal employees and stakeholders

Industry/Entity Type

Business Management, Finance, Accounting

Requirements
Must have
• Maintain a fortress, temple, or pyramid schema
Nice to have
• Scenic Background

```html
<!DOCTYPE html>
<html lang="en">
<head>
<meta charset="UTF-8">
<title>Business Management Fortress</title>
<link rel="stylesheet" href="https://fonts.googleapis.com/css2?family=Oswald:wght@500;600&display=swap">
<style>
  :root{
    --navy:#10295e;
    --bg-light:#3d8fd0;
    --bg-dark:#0b3c8c;
    --stone-light:#d9d9d9;
    --stone-mid:#a9a9a9;
    --stone-dark:#7f7f7f;
    --people:#fdbf00;
    --people-dark:#b88700;
    --innovation:#ed7d31;
    --innovation-dark:#c0521a;
    --intel:#70ad47;
    --intel-dark:#4b7a2c;
    --alliance:#5b9bd5;
    --alliance-dark:#2f72b5;
    --alliance-shaft:#1fa7e0;
    --white:#ffffff;
  }
  html,body{margin:0;padding:0;overflow:hidden;}
  .slide{
    position:relative;width:1200px;height:675px;overflow:hidden;
    font-family:'Oswald',sans-serif;
  }
  .scene-backdrop{
    position:absolute;inset:0;
    background:
      radial-gradient(ellipse at 20% 30%, rgba(120,190,240,.55), transparent 60%),
      radial-gradient(ellipse at 80% 80%, rgba(10,40,110,.6), transparent 60%),
      linear-gradient(120deg,var(--bg-light),var(--bg-dark));
  }
  .roof{position:absolute;left:0;top:0;}
  .roof-label{
    position:absolute;color:var(--navy);font-weight:600;font-size:27px;
    letter-spacing:3px;transform:translateX(-50%);line-height:1;
  }
  .beam{
    position:absolute;left:180px;top:214px;width:823px;height:37px;border-radius:19px;
    background:linear-gradient(180deg,#b5b5b5,#9c9c9c);
    box-shadow:0 4px 8px rgba(0,0,0,.35);
  }
  .pillar{position:absolute;top:251px;width:165px;height:292px;}
  .pillar .cap-top,.pillar .foot-bottom{position:absolute;left:31px;width:103px;}
  .pillar .cap-top{top:0;height:10px;}
  .pillar .cap-inner,.pillar .foot-inner{position:absolute;left:40px;width:85px;height:13px;}
  .pillar .cap-inner{top:10px;}
  .pillar .shaft{position:absolute;left:54px;top:23px;width:57px;height:235px;border-radius:14px;}
  .pillar .foot-inner{top:258px;}
  .pillar .foot-bottom{top:273px;height:19px;border-radius:2px;}
  .panel{
    position:absolute;left:0;top:60px;width:165px;height:171px;border-radius:5px;
    display:flex;flex-direction:column;align-items:center;
    box-shadow:0 3px 8px rgba(0,0,0,.25);
  }
  .panel .icon{
    width:60px;height:56px;margin-top:22px;border-radius:6px;
    background:rgba(255,255,255,.35);
  }
  .panel .pillar-name{
    flex:1;display:flex;align-items:center;text-align:center;
    color:var(--white);font-weight:500;font-size:26px;line-height:25px;
    text-shadow:1px 2px 3px rgba(0,0,0,.35);padding-bottom:22px;
  }
  .people{left:198px;} .innovation{left:407px;} .intel{left:616px;} .alliance{left:824px;}
  .people .panel{background:var(--people);}
  .people .cap-top,.people .foot-bottom{background:var(--people-dark);}
  .people .cap-inner,.people .foot-inner{background:var(--people);}
  .people .shaft{background:linear-gradient(90deg,#6b5000,#c79400 45%,#6b5000);}
  .innovation .panel{background:var(--innovation);}
  .innovation .cap-top,.innovation .foot-bottom{background:var(--innovation-dark);}
  .innovation .cap-inner,.innovation .foot-inner{background:var(--innovation);}
  .innovation .shaft{background:linear-gradient(90deg,#7a3008,#e3692a 45%,#7a3008);}
  .intel .panel{background:var(--intel);}
  .intel .cap-top,.intel .foot-bottom{background:var(--intel-dark);}
  .intel .cap-inner,.intel .foot-inner{background:var(--intel);}
  .intel .shaft{background:linear-gradient(90deg,#1f3a10,#4f8a2c 45%,#1f3a10);}
  .alliance .panel{background:var(--alliance);}
  .alliance .cap-top,.alliance .foot-bottom{background:var(--alliance-dark);}
  .alliance .cap-inner,.alliance .foot-inner{background:var(--alliance);}
  .alliance .shaft{background:linear-gradient(90deg,#0a3a66,var(--alliance-shaft) 45%,#0a3a66);}
  .foundation{
    position:absolute;left:169px;top:543px;width:832px;height:33px;border-radius:4px;
    background:linear-gradient(90deg,var(--stone-light),var(--stone-dark));
    display:flex;align-items:center;justify-content:center;
    color:var(--navy);font-weight:600;font-size:21px;letter-spacing:4px;
    box-shadow:0 3px 6px rgba(0,0,0,.3);
  }
  .foundation-base{
    position:absolute;left:152px;top:577px;width:861px;height:40px;border-radius:4px;
    background:linear-gradient(90deg,#e0e0e0,#8c8c8c);
    display:flex;align-items:center;justify-content:center;
    color:var(--navy);font-weight:500;font-size:14.5px;
    box-shadow:0 3px 6px rgba(0,0,0,.3);
  }
</style>
</head>
<body>
<div class="slide">
  <div class="scene-backdrop" role="img" aria-label="Blurred office workspace photo in blue tones"></div>

  <svg class="roof" width="1200" height="675" viewBox="0 0 1200 675" aria-hidden="true">
    <defs>
      <linearGradient id="stone" x1="0" y1="0" x2="1" y2="0">
        <stop offset="0" stop-color="#e6e6e6"/>
        <stop offset="1" stop-color="#8e8e8e"/>
      </linearGradient>
    </defs>
    <polygon points="593,54 188,216 1003,216" fill="#8a8a8a"/>
    <polygon points="593,64 225,210 966,210" fill="url(#stone)"/>
    <polygon points="405,131 196,214 583,214" fill="#8a8a8a"/>
    <polygon points="405,141 232,209 560,209" fill="url(#stone)"/>
    <polygon points="786,131 602,214 1000,214" fill="#8a8a8a"/>
    <polygon points="786,141 625,209 965,209" fill="url(#stone)"/>
  </svg>
  <div class="roof-label" style="left:583px;top:106px;">PARTNER</div>
  <div class="roof-label" style="left:400px;top:166px;">LEADER</div>
  <div class="roof-label" style="left:786px;top:166px;">PROFIT</div>

  <div class="beam"></div>

  <div class="pillar people">
    <div class="cap-top"></div><div class="cap-inner"></div><div class="shaft"></div>
    <div class="foot-inner"></div><div class="foot-bottom"></div>
    <div class="panel"><div class="icon" role="img" aria-label="Family icon"></div><div class="pillar-name">PEOPLE</div></div>
  </div>
  <div class="pillar innovation">
    <div class="cap-top"></div><div class="cap-inner"></div><div class="shaft"></div>
    <div class="foot-inner"></div><div class="foot-bottom"></div>
    <div class="panel"><div class="icon" role="img" aria-label="Puzzle pieces icon"></div><div class="pillar-name">INNOVATION</div></div>
  </div>
  <div class="pillar intel">
    <div class="cap-top"></div><div class="cap-inner"></div><div class="shaft"></div>
    <div class="foot-inner"></div><div class="foot-bottom"></div>
    <div class="panel"><div class="icon" role="img" aria-label="Head with gears icon"></div><div class="pillar-name">BUSINESS<br>INTELLIGENCE</div></div>
  </div>
  <div class="pillar alliance">
    <div class="cap-top"></div><div class="cap-inner"></div><div class="shaft"></div>
    <div class="foot-inner"></div><div class="foot-bottom"></div>
    <div class="panel"><div class="icon" role="img" aria-label="Strategy board icon"></div><div class="pillar-name">STRATEGIC<br>ALLIANCES</div></div>
  </div>

  <div class="foundation">FIDUCIARY RESPONSIBILITIES</div>
  <div class="foundation-base">ACCURATE FINANCIALS / INTERNAL CONTROLS / BRAND PROTECTION / COMPLIANCE / ETHICS / COST MANAGEMENT</div>
</div>
</body>
</html>
```